WardPeak landing page

The existing website at www.wardpeak-example.com needs updating. I've attached some marketing material for the color scheme to be used and potential content. The tagline should be "Real-Time Operational Intelligence." I want the landing page to be in 3 categories in this order and features within each category. Plenty of images are preferred and wording can be modified.
Wardpeak Command Centre
- Live Incident tracking and reporting with escalation on critical incidents if necessary
- Geofence Monitoring to ensure guards at the right location at the right time.
- Smart scheduling to ensure the correct training and certifications are assigned to the appropriate guard required.
- Camera compatibility to capture live and historical video for incident reporting
WardPeak Back Office Administration
- Automate Police report filing using data from submitted incidents when required.
- Track all required KPIs on a per site basis such as vehicle inspections, patrol tour details, etc
- Payroll and Invoicing using smart shift reports
- Create and manage client sites with configurable geofencing
WardPeak App
- Guard can see all site details and instructions when logging onto shift
- Ability to view all incidents that have occured at that particular site over the last 'x' days. Understand what has been happening and when.
- Report incidents with all relevant information including photo and video
- Recieve alerts when repeat offences are occuring within a configurable vicinity.

Target Market(s)

Retailers and guard companies

Coding

Coded - Design and coding required

Number of Pages Required

1 page

Requirements
Nice to have
• Use the look and feel of the logo in the design

```html
<!DOCTYPE html>
<html lang="en">
<head>
<meta charset="utf-8">
<title>WardPeak — Real-Time Operational Intelligence</title>
<link href="https://fonts.googleapis.com/css2?family=Inter:wght@400;500;600;700;800&display=swap" rel="stylesheet">
<style>
:root{
  --navy:#1c2b5e;
  --navy-deep:#17244f;
  --blue:#2f80e4;
  --blue-soft:#e6effc;
  --ink:#16213f;
  --muted:#7a8296;
  --line:#e6e9f0;
  --bg-soft:#f5f7fb;
  --green:#22b35e;
  --red:#e5484d;
  --amber:#e9a23b;
  --white:#ffffff;
}
*{box-sizing:border-box;margin:0;padding:0}
html,body{width:1200px;height:4054px;overflow:hidden}
body{font-family:'Inter',sans-serif;color:var(--ink);background:var(--white);position:relative}
.wrap{width:822px;margin:0 auto;position:relative}
.section{position:relative;overflow:hidden}
.tag{display:inline-flex;align-items:center;gap:6px;background:var(--blue-soft);color:var(--blue);font-size:9px;font-weight:600;padding:4px 9px;border-radius:10px}
.tag .num{color:var(--navy)}
.btn{display:inline-flex;align-items:center;justify-content:center;gap:8px;font-size:11px;font-weight:600;border-radius:7px;height:38px;padding:0 22px}
.btn-primary{background:var(--navy);color:var(--white)}
.btn-ghost{background:var(--white);color:var(--navy);border:1px solid var(--line)}

/* Nav */
.nav{position:absolute;top:13px;left:216px;width:767px;height:42px;background:var(--white);border-radius:9px;box-shadow:0 4px 18px rgba(28,43,94,.1);display:flex;align-items:center;padding:0 16px;z-index:5}
.brand{display:flex;align-items:center;gap:6px;font-weight:700;font-size:11px;color:var(--navy)}
.brand .mark{width:16px;height:16px;border-radius:4px;background:var(--blue)}
.nav-links{display:flex;gap:20px;font-size:10px;color:var(--ink);margin-left:205px}
.nav-right{margin-left:auto;display:flex;align-items:center;gap:14px;font-size:10px}
.nav-right .btn{height:26px;padding:0 14px;font-size:9.5px;border-radius:6px}

/* Hero */
.hero{height:587px;background:linear-gradient(120deg,#ffffff 30%,#eef2fa 100%)}
.hero-copy{position:absolute;left:189px;top:108px;width:360px}
.hero h1{font-size:50px;line-height:49px;font-weight:800;letter-spacing:-1.2px;margin:18px 0 20px;color:var(--navy)}
.hero h1 .accent{color:var(--blue)}
.hero p{font-size:12px;line-height:20px;color:var(--muted);width:320px}
.hero-actions{display:flex;gap:12px;margin-top:22px}
.stats{display:flex;gap:28px;margin-top:38px}
.stat b{display:block;font-size:20px;font-weight:700;color:var(--navy)}
.stat span{font-size:9px;color:var(--muted)}
.hero-photo{position:absolute;left:617px;top:164px;width:393px;height:280px;border-radius:14px;background:radial-gradient(circle at 30% 40%,#3c4a66 0,#1d2538 45%,#0f1522 100%)}
.alert-card{position:absolute;left:605px;top:183px;width:128px;height:42px;background:var(--white);border-radius:8px;box-shadow:0 6px 18px rgba(0,0,0,.15);display:flex;gap:7px;padding:8px;font-size:8px}
.alert-card .ico{width:18px;height:18px;border-radius:5px;background:#fdecec;flex:none}
.alert-card b{display:block;font-size:8px;color:var(--ink)}
.alert-card span{color:var(--muted);font-size:6.5px}
.laptop{position:absolute;left:592px;top:354px;width:186px;height:108px;background:#2b3550;border-radius:6px 6px 0 0;padding:5px}
.laptop-base{position:absolute;left:580px;top:462px;width:212px;height:8px;background:#c7ccd6;border-radius:0 0 6px 6px}
.screen{background:var(--white);height:100%;border-radius:3px;overflow:hidden}
.screen-bar{height:9px;background:var(--navy)}
.screen-stats{display:flex;gap:4px;padding:4px}
.screen-stats div{flex:1;background:#f4f6fa;border-radius:3px;text-align:center;font-size:11px;font-weight:700;padding:4px 0;color:var(--navy)}
.screen-stats div:last-child{color:var(--red)}
.screen-map{margin:0 4px;height:38px;background:#e5f3e8;border-radius:3px;position:relative}

/* Trusted */
.trusted{height:71px;background:var(--bg-soft);border-top:1px solid var(--line);border-bottom:1px solid var(--line)}
.trusted .wrap{display:flex;align-items:center;height:100%}
.trusted small{font-size:8.5px;letter-spacing:1.2px;color:var(--muted);font-weight:600}
.trusted ul{list-style:none;display:flex;gap:26px;margin-left:auto;font-size:12px;font-weight:600;color:#9aa6be}

/* Feature rows */
.feature{height:476px}
.feature.soft{background:var(--bg-soft);height:472px}
.photo{position:absolute;border-radius:12px}
.feature-copy{position:absolute;width:390px}
.feature-copy h2{font-size:24px;font-weight:700;color:var(--navy);margin:12px 0 10px;letter-spacing:-.4px}
.feature-copy .lead{font-size:12px;color:var(--muted);margin-bottom:24px}
.item{display:flex;gap:14px;margin-bottom:17px}
.item .ico{width:24px;height:24px;border-radius:6px;background:var(--blue-soft);flex:none;display:flex;align-items:center;justify-content:center}
.item h3{font-size:11px;font-weight:600;color:var(--navy);margin-bottom:5px}
.item p{font-size:9.5px;line-height:15px;color:var(--muted)}

.mini-card{position:absolute;background:var(--white);border-radius:8px;box-shadow:0 6px 18px rgba(0,0,0,.14);padding:9px;font-size:8px}

/* Back office laptop */
.bo-laptop{position:absolute;left:661px;top:121px;width:316px;height:218px;background:#c9ced8;border-radius:6px 6px 0 0;padding:4px}
.bo-base{position:absolute;left:646px;top:339px;width:340px;height:10px;background:#c1c6d0;border-radius:0 0 7px 7px}
.bo-screen{display:flex;height:100%;background:var(--white)}
.bo-side{width:82px;background:var(--navy);padding:10px 5px}
.bo-side i{display:block;height:6px;width:40px;background:rgba(255,255,255,.25);border-radius:2px;margin:14px 6px}
.bo-side i.on{background:var(--blue);width:70px;height:14px;margin:10px 0}
.bo-main{flex:1;padding:10px;font-size:7px;font-weight:700;color:var(--ink)}
.bo-cols{display:flex;gap:10px;margin-top:8px}
.bo-cols div{flex:1}
.field{height:8px;border:1px solid var(--line);border-radius:2px;margin:12px 0 0}
.bo-submit{height:16px;background:var(--green);border-radius:3px;margin-top:18px}

/* Phone */
.phone{position:absolute;left:121px;top:224px;width:148px;height:184px;background:#1a1f2c;border-radius:18px;padding:6px}
.phone-screen{background:var(--white);height:100%;border-radius:13px;overflow:hidden;padding:0 0 8px}
.phone-head{height:20px;background:var(--navy);color:var(--white);font-size:6px;text-align:center;line-height:20px;font-weight:600}
.phone-body{padding:8px}
.upload{height:34px;border:1px dashed #cfd5e0;border-radius:4px}
.phone-btn{height:20px;background:var(--blue);border-radius:4px;margin-top:18px;color:var(--white);font-size:6px;text-align:center;line-height:20px}

/* Banner */
.banner{height:213px;background:var(--navy);text-align:center;color:var(--white)}
.banner h2{font-size:24px;font-weight:700;padding-top:66px;letter-spacing:-.3px}
.banner p{font-size:12px;line-height:19px;color:#c7d1ea;width:400px;margin:10px auto 0}

/* How it works */
.how{height:467px;text-align:center}
.sec-head{padding-top:67px}
.sec-head h2{font-size:24px;font-weight:700;color:var(--navy);margin:12px 0 8px;letter-spacing:-.4px}
.sec-head p{font-size:12px;color:var(--muted)}
.steps{display:flex;gap:22px;margin-top:45px;text-align:left}
.step{width:189px}
.step .photo{position:static;height:106px;border-radius:6px}
.step .n{font-size:20px;font-weight:700;color:#c9daf4;margin-top:10px}
.step h3{font-size:12px;font-weight:600;color:var(--navy);margin:2px 0 6px}
.step p{font-size:9.5px;line-height:15px;color:var(--muted)}

/* Pricing */
.pricing{height:604px;background:var(--bg-soft);text-align:center}
.plans{display:flex;gap:19px;margin-top:45px;text-align:left}
.plan{width:261px;height:347px;background:var(--white);border-radius:10px;border:1px solid var(--line);padding:24px 21px;position:relative;display:flex;flex-direction:column}
.plan.pop{border:2px solid #bcd3f3}
.plan .badge{position:absolute;top:-8px;left:50%;transform:translateX(-50%);background:var(--blue);color:var(--white);font-size:7.5px;font-weight:600;padding:3px 9px;border-radius:8px}
.plan h3{font-size:13px;font-weight:600;color:var(--navy)}
.price{font-size:24px;font-weight:700;color:var(--navy);margin:12px 0 6px}
.price small{font-size:10px;color:var(--muted);font-weight:400}
.plan .desc{font-size:9px;line-height:14px;color:var(--muted);margin-bottom:18px}
.plan ul{list-style:none;font-size:9.5px;color:#4b5368}
.plan li{display:flex;gap:10px;align-items:center;height:21px}
.plan li svg{flex:none}
.plan .btn{margin-top:auto;height:30px;font-size:9.5px;width:100%}

/* CTA */
.cta{height:448px}
.response{position:absolute;left:233px;top:344px;width:174px;height:58px;display:flex;gap:12px;align-items:center;padding:0 12px}
.response .chk{width:26px;height:26px;border-radius:50%;background:#e3f6ea;flex:none}
.response b{display:block;font-size:9px;color:var(--navy)}
.response span{font-size:7px;color:var(--muted)}
.contact-line{display:flex;gap:10px;align-items:center;font-size:9.5px;color:var(--muted);margin-top:11px}

/* Footer */
.footer{height:243px;background:var(--navy);color:#aeb9d6}
.foot-cols{display:flex;padding-top:48px}
.foot-col{width:212px;font-size:9.5px}
.foot-col .brand{color:var(--white);margin-bottom:14px}
.foot-col p{line-height:15px;width:170px}
.foot-col h4{color:var(--white);font-size:10px;font-weight:600;margin-bottom:14px}
.foot-col li{list-style:none;margin-bottom:10px}
.foot-bottom{position:absolute;left:0;top:200px;width:100%;font-size:8.5px;color:#7f8bb0}
</style>
</head>
<body>

<nav class="nav">
  <div class="brand"><span class="mark"></span>WardPeak</div>
  <div class="nav-links"><span>Home</span><span>Features</span><span>Pricing</span><span>Contact</span></div>
  <div class="nav-right"><span>Login</span><span class="btn btn-primary">Request Demo</span></div>
</nav>

<header class="section hero">
  <div class="hero-copy">
    <span class="tag">● Security Operations Platform</span>
    <h1>Real-Time<br><span class="accent">Operational</span><br>Intelligence.</h1>
    <p>The all-in-one platform that gives security companies complete command over their operations — from the control room to the guard on the ground.</p>
    <div class="hero-actions">
      <span class="btn btn-primary">Request a Demo →</span>
      <span class="btn btn-ghost">Explore Features</span>
    </div>
    <div class="stats">
      <div class="stat"><b>99.9%</b><span>Uptime SLA</span></div>
      <div class="stat"><b>&lt;2s</b><span>Alert Latency</span></div>
      <div class="stat"><b>500+</b><span>Sites Managed</span></div>
      <div class="stat"><b>10K+</b><span>Guards Connected</span></div>
    </div>
  </div>
  <div class="hero-photo" role="img" aria-label="Operators typing at keyboards in a dim control room"></div>
  <div class="alert-card"><span class="ico"></span><div><b>Critical Alert</b><span>Perimeter breach — Zone B</span></div></div>
  <div class="laptop"><div class="screen">
    <div class="screen-bar"></div>
    <div class="screen-stats"><div>24</div><div>8</div></div>
    <div class="screen-map"></div>
  </div></div>
  <div class="laptop-base"></div>
</header>

<section class="section trusted">
  <div class="wrap">
    <small>TRUSTED BY SECURITY LEADERS</small>
    <ul><li>NorthGate</li><li>KeyHold</li><li>Lookfield</li><li>BastionCo</li><li>Sentrylane</li></ul>
  </div>
</section>

<section class="section feature">
  <div class="wrap">
    <div class="photo" role="img" aria-label="Hand holding a phone beside a smart door lock" style="left:0;top:106px;width:389px;height:266px;background:linear-gradient(90deg,#e8e9ea 0%,#cfd2d4 35%,#2e3a2c 60%,#1c2420 100%)"></div>
    <div class="mini-card" style="left:295px;top:300px;width:110px;height:80px">
      <b style="font-size:8px;color:var(--navy)">Live Dashboard</b><div style="color:var(--muted);font-size:6px">All sites monitored</div>
      <div style="display:flex;gap:6px;margin-top:10px;text-align:center;font-weight:700;font-size:10px">
        <div style="flex:1;background:#e9f7ef;color:var(--green);border-radius:4px;padding:3px 0">18</div>
        <div style="flex:1;background:#fdf4e4;color:var(--amber);border-radius:4px;padding:3px 0">3</div>
        <div style="flex:1;background:#fdecec;color:var(--red);border-radius:4px;padding:3px 0">1</div>
      </div>
    </div>
    <div class="feature-copy" style="left:433px;top:68px">
      <span class="tag"><span class="num">01</span>Command Centre</span>
      <h2>WardPeak Command Centre</h2>
      <p class="lead">Complete situational awareness from a single pane of glass</p>
      <div class="item"><span class="ico"><svg width="12" height="12" viewBox="0 0 12 12"><rect x="2" y="1.5" width="8" height="9" rx="1.5" fill="none" stroke="#2f80e4" stroke-width="1.2"/></svg></span><div><h3>Live Incident Tracking &amp; Reporting</h3><p>Track and report incidents in real-time with automatic escalation on critical events. Never miss a high-priority alert.</p></div></div>
      <div class="item"><span class="ico"><svg width="12" height="12" viewBox="0 0 12 12"><circle cx="6" cy="5" r="3" fill="none" stroke="#2f80e4" stroke-width="1.2"/><path d="M6 8v3" stroke="#2f80e4" stroke-width="1.2"/></svg></span><div><h3>Geofence Monitoring</h3><p>Ensure guards are at the right location at the right time with visual boundaries and automated compliance logging.</p></div></div>
      <div class="item"><span class="ico"><svg width="12" height="12" viewBox="0 0 12 12"><rect x="1.5" y="2.5" width="9" height="8" rx="1.5" fill="none" stroke="#2f80e4" stroke-width="1.2"/><path d="M1.5 5h9" stroke="#2f80e4" stroke-width="1.2"/></svg></span><div><h3>Smart Scheduling</h3><p>Intelligent shift assignment matching guard certifications, training records and clearance levels to site requirements.</p></div></div>
      <div class="item"><span class="ico"><svg width="12" height="12" viewBox="0 0 12 12"><rect x="1" y="3" width="7" height="6" rx="1" fill="none" stroke="#2f80e4" stroke-width="1.2"/><path d="M8 5l3-1.5v5L8 7" fill="none" stroke="#2f80e4" stroke-width="1.2"/></svg></span><div><h3>Camera Compatibility</h3><p>Integrate with on-site cameras for live and historical video. Attach footage directly to incident reports.</p></div></div>
    </div>
  </div>
</section>

<section class="section feature soft">
  <div class="wrap">
    <div class="feature-copy" style="left:0;top:66px;width:400px">
      <span class="tag"><span class="num">02</span>Back Office</span>
      <h2>WardPeak Back Office</h2>
      <p class="lead">Streamline administration and eliminate manual busywork</p>
      <div class="item"><span class="ico"><svg width="12" height="12" viewBox="0 0 12 12"><rect x="2" y="1.5" width="8" height="9" rx="1.5" fill="none" stroke="#2f80e4" stroke-width="1.2"/></svg></span><div><h3>Automated Police Report Filing</h3><p>Generate and file police reports automatically using data from submitted incidents — saving hours weekly.</p></div></div>
      <div class="item"><span class="ico"><svg width="12" height="12" viewBox="0 0 12 12"><path d="M2 10V6M5 10V3M8 10V5" stroke="#2f80e4" stroke-width="1.4"/></svg></span><div><h3>KPI Tracking Per Site</h3><p>Monitor all required KPIs per site — vehicle inspections, patrol tour details, checkpoint completions and custom metrics.</p></div></div>
      <div class="item"><span class="ico"><svg width="12" height="12" viewBox="0 0 12 12"><circle cx="6" cy="6" r="4.5" fill="none" stroke="#2f80e4" stroke-width="1.2"/></svg></span><div><h3>Payroll &amp; Invoicing</h3><p>Smart shift reports feed directly into payroll and client invoicing. Eliminate double-entry and billing disputes.</p></div></div>
      <div class="item"><span class="ico"><svg width="12" height="12" viewBox="0 0 12 12"><rect x="2.5" y="1.5" width="7" height="9" fill="none" stroke="#2f80e4" stroke-width="1.2"/></svg></span><div><h3>Client Site Management</h3><p>Create and manage client sites with configurable geofencing, custom instructions and compliance requirements.</p></div></div>
    </div>
  </div>
  <div class="bo-laptop"><div class="bo-screen">
    <div class="bo-side"><i class="on"></i><i></i><i></i><i></i><i></i><i></i><i></i></div>
    <div class="bo-main">Police Reports
      <div class="bo-cols">
        <div>New Incident<div class="field"></div><div class="field"></div><div class="field"></div><div class="field"></div><div class="field"></div></div>
        <div>Case Management<div class="field"></div><div class="field"></div><div class="field"></div><div class="bo-submit"></div></div>
      </div>
    </div>
  </div></div>
  <div class="bo-base"></div>
</section>

<section class="section feature" style="height:473px">
  <div class="wrap">
    <div class="photo" role="img" aria-label="Hand signing a paper document on a wooden desk" style="left:0;top:87px;width:389px;height:299px;background:linear-gradient(135deg,#c98a4a 0%,#e9e3da 45%,#d8d2c9 70%,#b77a3f 100%)"></div>
    <div class="phone"><div class="phone-screen">
      <div class="phone-head">Incident Reporting</div>
      <div class="phone-body">
        <div class="upload"></div>
        <div style="font-size:5px;font-weight:700;margin-top:10px">Description</div>
        <div class="field" style="margin-top:4px;height:18px"></div>
        <div style="display:flex;gap:6px;margin-top:6px"><div class="field" style="flex:1;height:16px;margin:0"></div><div class="field" style="flex:1;height:16px;margin:0"></div></div>
        <div class="phone-btn">Submit Report</div>
      </div>
    </div></div>
    <div class="feature-copy" style="left:433px;top:64px">
      <span class="tag"><span class="num">03</span>Mobile App</span>
      <h2>WardPeak App</h2>
      <p class="lead">Everything your guards need — right in their pocket</p>
      <div class="item"><span class="ico"><svg width="12" height="12" viewBox="0 0 12 12"><rect x="2" y="1.5" width="8" height="9" rx="1.5" fill="none" stroke="#2f80e4" stroke-width="1.2"/></svg></span><div><h3>Site Details &amp; Instructions</h3><p>Guards see all site details and post orders the moment they log onto shift. No confusion, no missed protocols.</p></div></div>
      <div class="item"><span class="ico"><svg width="12" height="12" viewBox="0 0 12 12"><circle cx="6" cy="6" r="4.5" fill="none" stroke="#2f80e4" stroke-width="1.2"/><path d="M6 3.5V6l2 1" fill="none" stroke="#2f80e4" stroke-width="1.2"/></svg></span><div><h3>Incident History</h3><p>View all incidents at a site over a configurable period. Understand what happened, when and who was involved.</p></div></div>
      <div class="item"><span class="ico"><svg width="12" height="12" viewBox="0 0 12 12"><rect x="1" y="3" width="7" height="6" rx="1" fill="none" stroke="#2f80e4" stroke-width="1.2"/><path d="M8 5l3-1.5v5L8 7" fill="none" stroke="#2f80e4" stroke-width="1.2"/></svg></span><div><h3>Rich Incident Reporting</h3><p>Report incidents with photos, video, GPS location, timestamps and witness details — submitted in seconds.</p></div></div>
      <div class="item"><span class="ico"><svg width="12" height="12" viewBox="0 0 12 12"><path d="M3 8.5V5.5a3 3 0 016 0v3l1 1H2z" fill="none" stroke="#2f80e4" stroke-width="1.2"/></svg></span><div><h3>Repeat Offence Alerts</h3><p>Receive intelligent alerts when repeat offences occur within a configurable vicinity. Spot patterns early.</p></div></div>
    </div>
  </div>
</section>

<section class="section banner" role="img" aria-label="Row of security cameras on a dark brick wall, tinted navy">
  <h2>One platform. Complete control.</h2>
  <p>From the command centre to the field — WardPeak connects every part of your security operation in real time.</p>
</section>

<section class="section how">
  <div class="wrap">
    <div class="sec-head">
      <span class="tag">How It Works</span>
      <h2>Up and running in days, not months</h2>
      <p>A seamless onboarding process designed around your operations.</p>
    </div>
    <div class="steps">
      <div class="step"><div class="photo" role="img" aria-label="Bright open-plan office with desks" style="background:linear-gradient(180deg,#9fb2c4,#d9d2c4 60%,#7d8da0)"></div><div class="n">01</div><h3>Discovery Call</h3><p>We learn about your operations, sites, and pain points to configure WardPeak around your needs.</p></div>
      <div class="step"><div class="photo" role="img" aria-label="Laptop showing analytics charts" style="background:linear-gradient(160deg,#4b5566,#aeb6c2 55%,#3a4150)"></div><div class="n">02</div><h3>Platform Setup</h3><p>Your sites, geofences, guard roster and post orders are configured and ready to go.</p></div>
      <div class="step"><div class="photo" role="img" aria-label="Team gathered for a training session" style="background:linear-gradient(180deg,#d9dde3,#b8b4ab 55%,#2f3f5a)"></div><div class="n">03</div><h3>Team Training</h3><p>Hands-on training for your command centre operators and field guards.</p></div>
      <div class="step"><div class="photo" role="img" aria-label="Staff working in a brick-walled office" style="background:linear-gradient(180deg,#c89566,#a87352 50%,#4b6a8a)"></div><div class="n">04</div><h3>Go Live</h3><p>Launch with full support. Our team monitors your rollout and fine-tunes as needed.</p></div>
    </div>
  </div>
</section>

<section class="section pricing">
  <div class="wrap">
    <div class="sec-head" style="padding-top:62px">
      <span class="tag">Pricing</span>
      <h2>Plans that scale with you</h2>
      <p>No hidden fees. Cancel anytime. Volume discounts available.</p>
    </div>
    <div class="plans">
      <div class="plan">
        <h3>Starter</h3><div class="price">$299 <small>/month</small></div>
        <p class="desc">For small teams getting started with digital guard management.</p>
        <ul>
          <li><svg width="9" height="9" viewBox="0 0 9 9"><path d="M1 4.5l2.3 2.3L8 2" fill="none" stroke="#22b35e" stroke-width="1.3"/></svg>Up to 25 guards</li>
          <li><svg width="9" height="9" viewBox="0 0 9 9"><path d="M1 4.5l2.3 2.3L8 2" fill="none" stroke="#22b35e" stroke-width="1.3"/></svg>5 client sites</li>
          <li><svg width="9" height="9" viewBox="0 0 9 9"><path d="M1 4.5l2.3 2.3L8 2" fill="none" stroke="#22b35e" stroke-width="1.3"/></svg>Incident reporting</li>
          <li><svg width="9" height="9" viewBox="0 0 9 9"><path d="M1 4.5l2.3 2.3L8 2" fill="none" stroke="#22b35e" stroke-width="1.3"/></svg>Basic scheduling</li>
          <li><svg width="9" height="9" viewBox="0 0 9 9"><path d="M1 4.5l2.3 2.3L8 2" fill="none" stroke="#22b35e" stroke-width="1.3"/></svg>Mobile app access</li>
          <li><svg width="9" height="9" viewBox="0 0 9 9"><path d="M1 4.5l2.3 2.3L8 2" fill="none" stroke="#22b35e" stroke-width="1.3"/></svg>Email support</li>
        </ul>
        <span class="btn btn-ghost" style="background:var(--bg-soft)">Start Free Trial</span>
      </div>
      <div class="plan pop">
        <span class="badge">Most Popular</span>
        <h3>Professional</h3><div class="price">$699 <small>/month</small></div>
        <p class="desc">For growing security companies that need full operational control.</p>
        <ul>
          <li><svg width="9" height="9" viewBox="0 0 9 9"><path d="M1 4.5l2.3 2.3L8 2" fill="none" stroke="#22b35e" stroke-width="1.3"/></svg>Up to 100 guards</li>
          <li><svg width="9" height="9" viewBox="0 0 9 9"><path d="M1 4.5l2.3 2.3L8 2" fill="none" stroke="#22b35e" stroke-width="1.3"/></svg>Unlimited client sites</li>
          <li><svg width="9" height="9" viewBox="0 0 9 9"><path d="M1 4.5l2.3 2.3L8 2" fill="none" stroke="#22b35e" stroke-width="1.3"/></svg>Command Centre dashboard</li>
          <li><svg width="9" height="9" viewBox="0 0 9 9"><path d="M1 4.5l2.3 2.3L8 2" fill="none" stroke="#22b35e" stroke-width="1.3"/></svg>Geofence monitoring</li>
          <li><svg width="9" height="9" viewBox="0 0 9 9"><path d="M1 4.5l2.3 2.3L8 2" fill="none" stroke="#22b35e" stroke-width="1.3"/></svg>Payroll &amp; invoicing</li>
          <li><svg width="9" height="9" viewBox="0 0 9 9"><path d="M1 4.5l2.3 2.3L8 2" fill="none" stroke="#22b35e" stroke-width="1.3"/></svg>Camera integration</li>
          <li><svg width="9" height="9" viewBox="0 0 9 9"><path d="M1 4.5l2.3 2.3L8 2" fill="none" stroke="#22b35e" stroke-width="1.3"/></svg>Priority support</li>
        </ul>
        <span class="btn btn-primary">Start Free Trial</span>
      </div>
      <div class="plan">
        <h3>Enterprise</h3><div class="price">Custom</div>
        <p class="desc">For large operations requiring dedicated infrastructure and support.</p>
        <ul>
          <li><svg width="9" height="9" viewBox="0 0 9 9"><path d="M1 4.5l2.3 2.3L8 2" fill="none" stroke="#22b35e" stroke-width="1.3"/></svg>Unlimited guards</li>
          <li><svg width="9" height="9" viewBox="0 0 9 9"><path d="M1 4.5l2.3 2.3L8 2" fill="none" stroke="#22b35e" stroke-width="1.3"/></svg>Dedicated account manager</li>
          <li><svg width="9" height="9" viewBox="0 0 9 9"><path d="M1 4.5l2.3 2.3L8 2" fill="none" stroke="#22b35e" stroke-width="1.3"/></svg>Custom integrations</li>
          <li><svg width="9" height="9" viewBox="0 0 9 9"><path d="M1 4.5l2.3 2.3L8 2" fill="none" stroke="#22b35e" stroke-width="1.3"/></svg>API access</li>
          <li><svg width="9" height="9" viewBox="0 0 9 9"><path d="M1 4.5l2.3 2.3L8 2" fill="none" stroke="#22b35e" stroke-width="1.3"/></svg>On-premise option</li>
          <li><svg width="9" height="9" viewBox="0 0 9 9"><path d="M1 4.5l2.3 2.3L8 2" fill="none" stroke="#22b35e" stroke-width="1.3"/></svg>SLA guarantee</li>
          <li><svg width="9" height="9" viewBox="0 0 9 9"><path d="M1 4.5l2.3 2.3L8 2" fill="none" stroke="#22b35e" stroke-width="1.3"/></svg>24/7 phone support</li>
        </ul>
        <span class="btn btn-ghost" style="background:var(--bg-soft)">Contact Sales</span>
      </div>
    </div>
  </div>
</section>

<section class="section cta">
  <div class="wrap">
    <div class="photo" role="img" aria-label="Desk with plant, notebook and smart speaker beside a monitor" style="left:0;top:62px;width:389px;height:320px;background:linear-gradient(135deg,#2b3a2a 0%,#4a5a3e 35%,#2c4a86 65%,#1a2233 100%)"></div>
    <div class="mini-card response"><span class="chk"></span><div><b>Response within 24hrs</b><span>Our team will reach out fast</span></div></div>
    <div class="feature-copy" style="left:433px;top:118px;width:380px">
      <span class="tag">Get In Touch</span>
      <h2 style="line-height:28px">Ready to transform your operations?</h2>
      <p class="lead" style="line-height:19px">Book a personalised demo and see how WardPeak can give your team real-time operational intelligence.</p>
      <div style="display:flex;gap:12px"><span class="btn btn-primary">Request a Demo</span><span class="btn btn-ghost">Email Us</span></div>
      <div style="margin-top:14px">
        <div class="contact-line"><svg width="11" height="11" viewBox="0 0 11 11"><rect x="1" y="2" width="9" height="7" rx="1" fill="none" stroke="#2f80e4" stroke-width="1.1"/><path d="M1 2.5l4.5 3.5L10 2.5" fill="none" stroke="#2f80e4" stroke-width="1.1"/></svg>hello@wardpeak-example.com</div>
        <div class="contact-line"><svg width="11" height="11" viewBox="0 0 11 11"><path d="M2 1.5h2l1 2.5-1.3 1a6 6 0 002.3 2.3l1-1.3 2.5 1v2A1 1 0 018.5 10 8 8 0 011 2.5a1 1 0 011-1z" fill="none" stroke="#2f80e4" stroke-width="1.1"/></svg>1-800-555-0142</div>
      </div>
    </div>
  </div>
</section>

<footer class="section footer">
  <div class="wrap">
    <div class="foot-cols">
      <div class="foot-col"><div class="brand"><span class="mark"></span>WardPeak</div><p>Real-time operational intelligence for security companies that demand more.</p></div>
      <div class="foot-col"><h4>Platform</h4><ul><li>Command Centre</li><li>Back Office</li><li>Mobile App</li><li>Pricing</li></ul></div>
      <div class="foot-col"><h4>Company</h4><ul><li>About Us</li><li>Careers</li><li>Contact</li><li>Blog</li></ul></div>
      <div class="foot-col"><h4>Legal</h4><ul><li>Privacy Policy</li><li>Terms of Service</li><li>Security</li></ul></div>
    </div>
  </div>
  <div class="foot-bottom"><div class="wrap">© 2026 WardPeak. All rights reserved.</div></div>
</footer>

</body>
</html>
```